Financial industry/Advisor business card

I'm a Financial Advisor starting my own investment company, Brandvik Wealth Management. I currently use the 'Light Blue' color that's provided on the Cardmello web page, but I want something unique. I'd like to keep the color, but the design is up for grabs.

Industry/Entity Type

Business

Contact Information for Business Card

Brandvik Wealth Management
Dale R. Brandvik
President
5142 Gableston Ln
Ste 240
Hollis Bend Md 21478
555-555-0147-Office
555-555-0183-Fax
DBRANDVIK@BRANDVIKW.example

```html
<!DOCTYPE html>
<html lang="en">
<head>
<meta charset="utf-8">
<title>Brandvik Wealth Management – Business Card</title>
<link rel="stylesheet" href="https://fonts.googleapis.com/css2?family=Exo:wght@400;500&family=Arimo:wght@700&display=swap">
<style>
  :root {
    --brand-blue: #1b41c6;
    --title-blue: #1f46c9;
    --edge-cyan: #5fd3f0;
    --accent-orange: #e2581b;
    --paper: #ffffff;
  }
  html, body {
    margin: 0;
    padding: 0;
    width: 1200px;
    height: 702px;
    overflow: hidden;
    background: var(--paper);
  }
  .card {
    position: relative;
    width: 1200px;
    height: 702px;
    background: var(--paper);
    overflow: hidden;
  }
  .card-backdrop {
    position: absolute;
    inset: 0;
  }
  .contact-block {
    position: absolute;
    left: 0;
    top: 0;
    width: 540px;
    transform-origin: top left;
    transform: translate(92px, 618px) rotate(-90deg);
    color: var(--paper);
    font-family: "Arimo", Arial, sans-serif;
    font-weight: 700;
    font-style: normal;
  }
  .contact-line {
    display: block;
    font-size: 24px;
    line-height: 39px;
    letter-spacing: 1.5px;
    white-space: nowrap;
  }
  .contact-line--address {
    font-size: 20px;
    line-height: 29px;
    letter-spacing: 1px;
  }
  .brand {
    position: absolute;
    left: 421px;
    top: 152px;
    width: 712px;
  }
  .brand-name {
    margin: 0;
    font-family: "Exo", sans-serif;
    font-weight: 500;
    font-size: 84px;
    line-height: 1;
    color: var(--title-blue);
    white-space: nowrap;
    text-align: center;
    letter-spacing: 1px;
  }
  .brand-rule {
    height: 4px;
    margin-top: 6px;
    background: var(--title-blue);
  }
  .brand-tagline {
    margin: 8px 0 0 112px;
    font-family: "Arimo", Arial, sans-serif;
    font-weight: 700;
    font-size: 50px;
    letter-spacing: 17px;
    color: var(--accent-orange);
    line-height: 1.1;
    white-space: nowrap;
  }
  .name-plate {
    position: absolute;
    left: 674px;
    top: 573px;
    width: 486px;
    height: 92px;
    background: var(--brand-blue);
    text-align: center;
  }
  .person-name {
    margin: 10px 0 0 0;
    font-family: "Exo", sans-serif;
    font-weight: 500;
    font-size: 46px;
    line-height: 1;
    color: var(--paper);
    letter-spacing: 1px;
    white-space: nowrap;
  }
  .person-title {
    margin: 2px 0 0 0;
    font-family: "Arimo", Arial, sans-serif;
    font-weight: 700;
    font-size: 30px;
    letter-spacing: 8px;
    line-height: 1.1;
    color: var(--accent-orange);
  }
</style>
</head>
<body>
<main class="card">
  <svg class="card-backdrop" width="1200" height="702" viewBox="0 0 1200 702" aria-hidden="true">
    <path class="swoop-panel" d="M44 43 H281 C 292 420, 430 630, 674 657 V 665 H44 Z" fill="var(--brand-blue)"/>
    <path class="swoop-edge" d="M44 43 H281 C 292 420, 430 630, 674 657" fill="none" stroke="var(--edge-cyan)" stroke-width="3"/>
  </svg>

  <address class="contact-block">
    <span class="contact-line">Office 555-555-0147</span>
    <span class="contact-line">Fax 555-555-0183</span>
    <span class="contact-line">DBRANDVIK@BRANDVIKW.example</span>
    <span class="contact-line contact-line--address">5142 Gableston Ln Ste 240</span>
    <span class="contact-line contact-line--address">Hollis Bend Md 21478</span>
  </address>

  <header class="brand">
    <h1 class="brand-name">Brandvik Wealth</h1>
    <div class="brand-rule"></div>
    <p class="brand-tagline">Management</p>
  </header>

  <section class="name-plate">
    <p class="person-name">Dale R. Brandvik</p>
    <p class="person-title">President</p>
  </section>
</main>
</body>
</html>
```